Personal Injury Billboard for a law frim

Our firm has a billboard we need art for. It will specifically for personal injury cases. The dimensions of art the billboard are 9 ft high 29 feet wide.

We want to highlight the terms, "Serious Injuries" and "Trusted. Local. Experienced." We want to incorporate the attached "Brightvale Honors" badge as well as our attached firm logo. We want the blue color scheme (see attached).

Maybe an image of an industrial plant in the background?

Sans Serif

```html
<!DOCTYPE html>
<html lang="en">
<head>
<meta charset="utf-8">
<title>Serious Injuries Billboard – Harlow Benton Crane</title>
<link rel="stylesheet" href="https://fonts.googleapis.com/css2?family=Roboto+Slab:wght@900&family=Poppins:wght@600;700&family=Roboto+Condensed:wght@700&display=swap">
<style>
  :root {
    --page-bg: #d9dbdf;
    --board-white: #ffffff;
    --blue-bright: #2b83c9;
    --blue-deep: #1f4f8f;
    --navy: #1f2a5e;
    --tag-blue: #3385c6;
    --sky-light: #cfe3f4;
    --sky-mid: #a9cbe8;
    --plant-tone: #8a7a6c;
    --badge-orange: #f7901e;
  }
  html, body {
    margin: 0;
    padding: 0;
    width: 1143px;
    height: 1200px;
    overflow: hidden;
    background: var(--page-bg);
  }
  .canvas {
    width: 1143px;
    height: 1200px;
    display: flex;
    align-items: center;
    justify-content: center;
  }
  .billboard {
    width: 1060px;
    height: 329px;
    box-shadow: 0 14px 30px rgba(0,0,0,0.35);
    display: block;
  }
  .headline { font-family: "Roboto Slab", Georgia, serif; font-weight: 900; }
  .headline-light { fill: var(--board-white); font-size: 112px; }
  .headline-dark { fill: var(--navy); font-size: 112px; }
  .tagline { font-family: "Poppins", Arial, sans-serif; font-weight: 700; font-size: 22px; fill: var(--tag-blue); }
  .phone-number { font-family: "Roboto Condensed", Arial, sans-serif; font-weight: 700; font-size: 46px; fill: var(--board-white); }
  .firm-name { font-family: "Poppins", Arial, sans-serif; font-weight: 700; fill: var(--navy); }
</style>
</head>
<body>
<main class="canvas">
  <svg class="billboard" viewBox="0 0 1060 329" xmlns="http://www.w3.org/2000/svg" aria-label="Serious Injuries billboard for Harlow Benton Crane Attorneys">
    <defs>
      <linearGradient id="bandBlue" x1="0" y1="0" x2="1" y2="0">
        <stop offset="0" stop-color="var(--blue-bright)"/>
        <stop offset="1" stop-color="var(--blue-deep)"/>
      </linearGradient>
      <linearGradient id="plantTones" x1="0" y1="0" x2="0" y2="1">
        <stop offset="0" stop-color="var(--sky-light)"/>
        <stop offset="0.35" stop-color="var(--sky-mid)"/>
        <stop offset="0.6" stop-color="var(--plant-tone)"/>
        <stop offset="0.9" stop-color="#7f8f88"/>
        <stop offset="1" stop-color="#4f7a3c"/>
      </linearGradient>
    </defs>

    <rect class="board-bg" x="0" y="0" width="1060" height="329" fill="var(--board-white)"/>

    <!-- Industrial plant image band -->
    <polygon class="plant-image" points="543,0 865,0 1001,329 688,329" fill="url(#plantTones)"
             role="img" aria-label="Photograph of an industrial processing plant with pipes and towers against a blue sky"/>

    <!-- Headline -->
    <polygon class="headline-band" points="28,25 855,25 903,145 28,145" fill="url(#bandBlue)"/>
    <text class="headline headline-light" x="53" y="129" textLength="511" lengthAdjust="spacingAndGlyphs">SERIOUS</text>
    <text class="headline headline-dark" x="30" y="243" textLength="562" lengthAdjust="spacingAndGlyphs">INJURIES</text>

    <!-- Tagline -->
    <rect class="tagline-frame" x="28.5" y="259.5" width="559" height="40" fill="none" stroke="var(--blue-deep)" stroke-width="1"/>
    <text class="tagline" x="46" y="288" textLength="520" lengthAdjust="spacing">TRUSTED. LOCAL. EXPERIENCED.</text>

    <!-- Phone band -->
    <polygon class="phone-band" points="628,239 1015,239 1040,299 650,299" fill="url(#bandBlue)"/>
    <g class="phone-icon" fill="none" stroke="var(--board-white)" stroke-width="2" stroke-linecap="round" stroke-linejoin="round">
      <path d="M667,256 c-4,2 -5,6 -3,11 c3,7 8,12 15,15 c5,2 9,1 11,-3 l-5,-5 l-4,2 c-4,-2 -7,-5 -9,-9 l2,-4 z"/>
      <path d="M679,255 a10,10 0 0 1 9,9"/>
      <path d="M680,250 a15,15 0 0 1 13,13"/>
    </g>
    <line class="phone-divider" x1="700" y1="249" x2="700" y2="290" stroke="var(--board-white)" stroke-width="2"/>
    <text class="phone-number" x="710" y="287" textLength="291" lengthAdjust="spacingAndGlyphs">979-555-0148</text>

    <!-- Firm name -->
    <g class="firm-mark">
      <rect x="935" y="40" width="26" height="26" fill="var(--navy)"/>
      <text class="firm-name" x="966" y="62" font-size="22">HBC</text>
      <text class="firm-name" x="975" y="84" font-size="6.5" text-anchor="middle">www.hbc-law.com</text>
      <text class="firm-name" x="975" y="94" font-size="7.5" text-anchor="middle">HARLOW BENTON CRANE</text>
      <text class="firm-name" x="975" y="101" font-size="4.5" text-anchor="middle">ATTORNEYS</text>
    </g>

    <!-- Brightvale Honors badge -->
    <rect class="honors-badge" x="955" y="136" width="64" height="64" fill="var(--badge-orange)"
          role="img" aria-label="Brightvale Honors badge"/>
  </svg>
</main>
</body>
</html>
```